Buch-/E-Book-Cover für SEO Experte
Zielgruppe
SEO Experte Lorenz K. Abendroth ist Geschäftsführer einer SEO Agentur in Köln und bringt nun 'Das dicke Netzsuche & Webwerbung Handbuch' auf den Markt. ein kompaktes Werk welches alle Begrifflichkeiten und Konzepte aus der Welt der SEO Optimierung und des Online Marketings einfach erläutert zum nachschlagen in typischer Lexikon Manier.
Titel: Das dicke Netzsuche & Webwerbung Handbuch
Subtitel: Alle Fragen & Begriffe aus 6 Jahren SEO Agenturarbeit einfach erklärt und kompakt zusammengefasst zum nachschlagen
Aufgabenstellung
Es soll anders sein als das dazugehörige komplementär Buch 'Pixelhaus Ranking 2031' aber dennoch im selben Stil gearbeitet sein. Es soll wie ein sehr wertiges großes altes Lexikon wirken mit vielen Seiten. Bitte auch ein stehendes 3D Cover zum normalen Druck Cover liefern.

```html
<!DOCTYPE html>
<html lang="de">
<head>
<meta charset="utf-8">
<title>Das dicke Netzsuche &amp; Webwerbung Handbuch – Cover</title>
<link rel="stylesheet" href="https://fonts.googleapis.com/css2?family=Open+Sans:wght@400;700;800&display=swap">
<style>
  :root {
    --blue-deep: #2a6288;
    --blue-mid: #3580ad;
    --blue-text: #2f6a8e;
    --yellow: #f2c22e;
    --white: #ffffff;
    --floor-top: #e4e4e2;
    --floor-bottom: #f3f3f1;
  }
  html, body {
    margin: 0;
    padding: 0;
    width: 927px;
    height: 1200px;
    overflow: hidden;
    background: var(--blue-deep);
  }
  .cover {
    position: relative;
    width: 927px;
    height: 1200px;
    overflow: hidden;
    font-family: "Open Sans", Arial, sans-serif;
    background: radial-gradient(ellipse 60% 50% at 50% 42%, var(--blue-mid) 0%, var(--blue-deep) 100%);
  }
  .title {
    position: absolute;
    left: 0;
    top: 0;
    width: 927px;
    height: 660px;
  }
  .title text {
    font-family: "Open Sans", Arial, sans-serif;
    font-weight: 800;
  }
  .title .white { fill: var(--white); }
  .title .yellow { fill: var(--yellow); }
  .subtitle-box {
    position: absolute;
    left: 71px;
    top: 693px;
    width: 573px;
    height: 271px;
    box-sizing: border-box;
    border: 2px solid var(--white);
    padding: 26px 20px 0 26px;
    color: var(--white);
    font-size: 31px;
    line-height: 46px;
    font-weight: 400;
  }
  .subtitle-box strong {
    color: var(--yellow);
    font-weight: 700;
  }
  .floor {
    position: absolute;
    left: 0;
    top: 1029px;
    width: 927px;
    height: 171px;
    background: linear-gradient(180deg, var(--floor-top), var(--floor-bottom));
  }
  .rocket-art {
    position: absolute;
    left: 548px;
    top: 625px;
    width: 379px;
    height: 485px;
    background: radial-gradient(ellipse 45% 55% at 55% 60%, rgba(240,240,238,0.85) 0%, rgba(220,220,218,0.55) 45%, rgba(255,255,255,0) 75%);
  }
  .author {
    position: absolute;
    left: 0;
    top: 1124px;
    width: 927px;
    text-align: center;
    color: var(--blue-text);
    font-size: 20px;
    font-weight: 700;
    letter-spacing: 1.6px;
  }
</style>
</head>
<body>
  <main class="cover">
    <svg class="title" viewBox="0 0 927 660" aria-label="Das dicke Netzsuche &amp; Webwerbung Handbuch">
      <text class="white" x="77" y="175" font-size="146" textLength="776" lengthAdjust="spacingAndGlyphs">DAS DICKE</text>
      <text class="yellow" x="77" y="314" font-size="128" textLength="776" lengthAdjust="spacingAndGlyphs">NETZSUCHE &amp;</text>
      <text class="yellow" x="77" y="445" font-size="132" textLength="776" lengthAdjust="spacingAndGlyphs">WEBWERBUNG</text>
      <text class="white" x="77" y="622" font-size="200" textLength="776" lengthAdjust="spacingAndGlyphs">HANDBUCH</text>
    </svg>

    <div class="floor"></div>
    <div class="rocket-art" role="img" aria-label="Illustration: weiße Papierrakete startet mit Flamme aus aufbrechendem Boden"></div>

    <div class="subtitle-box">
      <strong>Alle Fragen</strong> und <strong>Begriffe</strong> aus 6&nbsp;Jahren SEO Agenturarbeit <strong>einfach erklärt</strong> und <strong>kompakt zusammengefasst</strong> zum nachschlagen.
    </div>

    <div class="author">LORENZ K. ABENDROTH</div>
  </main>
</body>
</html>
```